Design an Amazing Mailer for our Company

Using the copy and image ideas provided, create a 2-sided 12x15 mailer for our direct mail and print company to drive new customers to us. Be creative but keep the themes we want to go with in mind. Copy and sample images provided on the included file.

Target Market(s)

Small local businesses in our community

Industry/Entity Type

Direct Mail and Printing Company

Font styles to use
Serif
Sans Serif

Colors
0054AA
0677BA
7BADD7
CADEEF
E8F1F8
0094D4
00A9DD
6FCCEA
C7EBF8
E9F6FB

```html
<!DOCTYPE html>
<html lang="en">
<head>
<meta charset="utf-8">
<title>Northgate Direct Mail – Mailer</title>
<link href="https://fonts.googleapis.com/css2?family=Poppins:wght@300;400;500;600;800&family=Anton&family=Yellowtail&display=swap" rel="stylesheet">
<style>
:root{
  --stage:#1b2e4f;
  --navy:#0054AA;
  --blue:#0677BA;
  --mid:#7BADD7;
  --pale:#CADEEF;
  --mist:#E8F1F8;
  --sky:#0094D4;
  --cyan:#00A9DD;
  --aqua:#6FCCEA;
  --ice:#C7EBF8;
  --frost:#E9F6FB;
  --ink:#222;
  --red:#e0262f;
  --deep:#1c47a8;
}
*{margin:0;padding:0;box-sizing:border-box}
html,body{width:1200px;height:550px;overflow:hidden}
body{background:var(--stage);font-family:'Poppins',sans-serif;position:relative;color:var(--ink)}
.side{position:absolute;top:44px;width:541px;height:432px;background:#fff;overflow:hidden}
.side-front{left:47px}
.side-back{left:614px}
.abs{position:absolute}

/* brand stand-in */
.brand{position:absolute;display:flex;align-items:flex-start;gap:3px;font-weight:800;color:var(--navy);font-size:7px;line-height:8px;text-transform:uppercase;background:#fff;padding:4px}
.brand-mark{width:9px;height:9px;background:var(--navy);flex:none}
.front-brand{left:474px;top:11px;width:56px;height:50px}
.back-brand{left:461px;top:17px;width:60px;height:54px}

/* front */
.headline{left:29px;top:21px;font-weight:800;font-size:23.5px;line-height:24px;color:var(--blue);letter-spacing:-.3px}
.headline .light{color:var(--cyan)}
.neighbor-pill{left:26px;top:97px;width:202px;height:33px;border-radius:17px;background:var(--ice);color:var(--blue);font-weight:600;font-size:9.6px;line-height:11px;padding:5px 0 0 13px}
.years-for{left:27px;top:151px;font-family:'Yellowtail',cursive;color:var(--red);font-size:14px;line-height:16px}
.years-num{left:39px;top:132px;font-family:'Yellowtail',cursive;color:var(--red);font-size:56px;line-height:58px}
.years-word{left:92px;top:139px;font-family:'Yellowtail',cursive;color:var(--red);font-size:12px;line-height:14px}
.years-copy{left:92px;top:155px;width:170px;font-size:7.9px;line-height:9.6px}

.band-top{left:23px;top:197px;width:502px;height:102px;border-radius:16px 0 0 22px;background:linear-gradient(90deg,var(--navy),var(--blue) 55%,var(--sky) 80%,var(--aqua))}
.band-low{left:280px;top:290px;width:245px;height:126px;border-radius:0 0 22px 22px;background:linear-gradient(90deg,var(--blue),var(--sky) 60%,var(--aqua))}
.tab-whatwedo{left:23px;top:197px;width:138px;height:30px;background:var(--navy);border-radius:16px 0 18px 0;color:#fff;font-weight:800;font-size:14px;line-height:30px;padding-left:21px}

.sign-art{left:282px;top:23px;width:238px;height:200px;border-radius:20px;background:radial-gradient(ellipse at 55% 55%,#fbf4e8 0%,#f3dfc0 60%,#ead0a8 100%)}

.services{font-size:8.3px;line-height:11.2px;color:#fff;list-style:none}
.services li{position:relative;padding-left:14px}
.services svg{position:absolute;left:0;top:2px}
.services-left{left:44px;top:233px;width:255px}
.services-right{left:304px;top:233px;width:222px}

.address-box{left:23px;top:308px;width:243px;height:102px;border:1px solid #d9d9d9;border-radius:24px;background:#fff}
.offer{left:306px;top:287px;width:212px;color:#fff;font-size:8.5px;line-height:10.8px}
.offer b{font-weight:800}
.local-head{left:306px;top:352px;color:#fff;font-weight:500;font-size:13px;line-height:16px}
.local-copy{left:306px;top:372px;width:205px;color:#fff;font-size:7px;line-height:8.4px;font-weight:300}

/* back */
.corner-top{left:232px;top:0;width:309px;height:26px;background:var(--blue);border-radius:0 0 0 16px}
.corner-side{left:488px;top:0;width:53px;height:143px;background:var(--blue);border-radius:0 0 0 20px}
.service-head{left:240px;top:48px;width:230px;text-align:center;font-family:'Anton',sans-serif;color:var(--deep);font-size:25px;line-height:25px}
.we-do{left:240px;top:98px;width:230px;text-align:center;font-family:'Anton',sans-serif;color:var(--cyan);font-size:54px;line-height:56px}
.tray-photo{left:340px;top:150px;width:201px;height:188px;border-radius:30px 0 0 0;background:linear-gradient(160deg,#f1f2f4 0%,#e6d6c6 40%,#f3f3f3 65%,#5a5a5a 100%)}
.back-copy{left:30px;top:49px;font-size:7.7px;line-height:9.6px;color:#333}
.back-copy p{margin-bottom:9.6px}
.clients-tab{left:192px;top:315px;width:163px;height:26px;background:var(--navy);border-radius:16px 16px 0 0;color:#fff;font-weight:300;font-size:16px;text-align:center;line-height:28px}
.clients-band{left:0;top:339px;width:541px;height:93px;background:linear-gradient(90deg,var(--blue),var(--sky))}
.client-row{left:17px;top:351px;display:flex;gap:6px}
.client-card{width:67px;height:60px;background:#fff;border:1px solid var(--pale);display:flex;align-items:center;justify-content:center}
.client-art{width:36px;height:46px}
.client-names{left:17px;top:415px;display:flex;gap:6px}
.client-names span{width:67px;text-align:center;color:#fff;font-size:4.5px;line-height:5px;white-space:nowrap;display:flex;justify-content:center}
</style>
</head>
<body>

<section class="side side-front">
  <h1 class="abs headline">WHAT <span class="light">HAPPENS</span><br>IN BURBANK <span class="light">SHOULD</span><br>STAY IN BURBANK</h1>
  <p class="abs neighbor-pill">You’ve got a neighbor in the direct<br>mail business.</p>

  <span class="abs years-for">For</span>
  <span class="abs years-num">75</span>
  <span class="abs years-word">Years</span>
  <p class="abs years-copy">Northgate Direct Mail has been serving our community- from large studios to small mom-and-pop stores.</p>

  <div class="abs band-top"></div>
  <div class="abs band-low"></div>
  <div class="abs tab-whatwedo">WHAT WE DO</div>

  <div class="abs sign-art" role="img" aria-label="Illustration of a Burbank city limit road sign above a retro Las Vegas style marquee reading: What happens in Las Vegas stays in Las Vegas"></div>

  <div class="brand front-brand">
    <span class="brand-mark"></span><span>Northgate<br>Direct<br>Mail</span>
  </div>

  <ul class="abs services services-left">
    <li><svg width="8" height="8" viewBox="0 0 8 8"><circle cx="4" cy="4" r="4" fill="#C7EBF8"/><path d="M2 4.2l1.4 1.4L6 2.8" stroke="#0677BA" stroke-width="1" fill="none"/></svg>Direct Mail/Marketing</li>
    <li><svg width="8" height="8" viewBox="0 0 8 8"><circle cx="4" cy="4" r="4" fill="#C7EBF8"/><path d="M2 4.2l1.4 1.4L6 2.8" stroke="#0677BA" stroke-width="1" fill="none"/></svg>Mailing for Union Pension, Insurance, and Healthcare<br>Notices &amp; Membership Voting Materials</li>
    <li><svg width="8" height="8" viewBox="0 0 8 8"><circle cx="4" cy="4" r="4" fill="#C7EBF8"/><path d="M2 4.2l1.4 1.4L6 2.8" stroke="#0677BA" stroke-width="1" fill="none"/></svg>Nonprofit Mailing</li>
  </ul>
  <ul class="abs services services-right">
    <li><svg width="8" height="8" viewBox="0 0 8 8"><circle cx="4" cy="4" r="4" fill="#C7EBF8"/><path d="M2 4.2l1.4 1.4L6 2.8" stroke="#0677BA" stroke-width="1" fill="none"/></svg>Political and Community Campaign Mailing</li>
    <li><svg width="8" height="8" viewBox="0 0 8 8"><circle cx="4" cy="4" r="4" fill="#C7EBF8"/><path d="M2 4.2l1.4 1.4L6 2.8" stroke="#0677BA" stroke-width="1" fill="none"/></svg>City and Government Mailing</li>
    <li><svg width="8" height="8" viewBox="0 0 8 8"><circle cx="4" cy="4" r="4" fill="#C7EBF8"/><path d="M2 4.2l1.4 1.4L6 2.8" stroke="#0677BA" stroke-width="1" fill="none"/></svg>Fulfillment Services</li>
    <li><svg width="8" height="8" viewBox="0 0 8 8"><circle cx="4" cy="4" r="4" fill="#C7EBF8"/><path d="M2 4.2l1.4 1.4L6 2.8" stroke="#0677BA" stroke-width="1" fill="none"/></svg>*Green and Union options available</li>
  </ul>

  <div class="abs address-box"></div>

  <p class="abs offer">Mention this mailer and get a <b>$50 Gift Card</b> to Rosetti’s Bakery or Morning Grind Café on your first Order of <b>$2500 or more</b>; Get a <b>$100 Gift Card</b> to Rosetti’s Bakery or Corner Fresh Market on your first order of $5,000 or more.</p>
  <h2 class="abs local-head">We live here, too!</h2>
  <p class="abs local-copy">As a local family, we ascribe to the values that make our community special- that small town feel with big city services- focused on keeping us all connected.</p>
</section>

<section class="side side-back">
  <div class="abs corner-top"></div>
  <div class="abs corner-side"></div>
  <div class="brand back-brand">
    <span class="brand-mark"></span><span>Northgate<br>Direct<br>Mail</span>
  </div>

  <div class="abs tray-photo" role="img" aria-label="Photo of a waiter's hand holding a silver serving tray, white towel over the arm"></div>

  <h2 class="abs service-head">REMEMBER GREAT<br>CUSTOMER SERVICE?</h2>
  <p class="abs we-do">WE DO</p>

  <div class="abs back-copy">
    <p style="width:195px">We don’t provide a cookie-cutter mail service. We focus on helping clients by doing one thing really well—and that’s direct mail. Our team of experts goes through every phase of the direct mail cycle to provide you with better results, higher-value customers, and direct mailing success for years to come. We can design, print, mail, and provide targeted lists, tracking, and analytics. We’re more than a direct mail service provider, we’re your marketing partner!</p>
    <p style="width:205px">When you take these values and wrap them around our commitment to customer satisfaction, you get good old-fashioned customer service that is, sadly, rare these days.</p>
    <p style="width:280px">At Northgate Direct Mail, we view it as an obligation to our customers to go above and beyond to provide them with services that not only meet their needs but exceed their expectations. Our “Make it Right” mentality extends beyond our products and services.</p>
    <p style="width:300px">Whether it be the timely response to an inquiry, a human answering your call or following-up to ensure your ongoing satisfaction, you can trust that working with NDM will be a rewarding, enjoyable experience on top of an excellent return on your investment.</p>
  </div>

  <div class="abs clients-band"></div>
  <div class="abs clients-tab">Our Clients</div>

  <div class="abs client-row">
    <div class="client-card"><div class="client-art" style="background:linear-gradient(#3d3a5c,#b08a4a)" role="img" aria-label="Halloween event flyer"></div></div>
    <div class="client-card"><div class="client-art" style="height:14px;width:40px;background:var(--mist)" role="img" aria-label="Valley Ballclub name placeholder"></div></div>
    <div class="client-card"><div class="client-art" style="width:52px;height:36px;background:linear-gradient(90deg,#f7c6d9,#cde6f7)" role="img" aria-label="Reunion save-the-date postcard"></div></div>
    <div class="client-card"><div class="client-art" style="background:linear-gradient(#e9e9e9,#8a7a6a)" role="img" aria-label="Entertainment summit mailer"></div></div>
    <div class="client-card"><div class="client-art" style="background:linear-gradient(#6b7a5a,#3b4a3a)" role="img" aria-label="Film magazine cover"></div></div>
    <div class="client-card"><div class="client-art" style="background:linear-gradient(#3a4e6a,#a33b3b)" role="img" aria-label="Youth program poster"></div></div>
    <div class="client-card"><div class="client-art" style="background:linear-gradient(#c9302c,#e6b34a)" role="img" aria-label="Labor Day sale flyer"></div></div>
  </div>
  <div class="abs client-names">
    <span>Hillside Grocers</span><span></span><span>Valley Ballclub; Riverside Health Center</span><span>Screen Weekly</span><span>Frame &amp; Lens</span><span>Youth Club Alliance</span><span>Casa de Arte</span>
  </div>
</section>

</body>
</html>
```